Vera-Shine Janitorial Services

Looking for a modern design for my new business. I like the clear see through of the card I've attached. The business is built around The Pellmar Apex 720 system, with that said I'd like to add the pellmar logo on the bachside with the statement of Powered by (then the Pellmar Logo). I really like the layout and color schemes of the card I attached. Black, Blue, and White. I would like to incorporate three images into the diamond shape, as seem in the layout.

Gordon Pike
Managing Partner

Still waiting on revisions?

```html
<!DOCTYPE html>
<html lang="en">
<head>
<meta charset="utf-8">
<title>Vera-Shine Janitorial Services – Business Card</title>
<link href="https://fonts.googleapis.com/css2?family=Marcellus&family=Poppins:wght@400&family=Libre+Baskerville:wght@700&display=swap" rel="stylesheet">
<style>
  :root {
    --bg: #d9d9d9;
    --card-black: #111114;
    --card-white: #ffffff;
    --brand-blue: #2a6cc4;
    --accent-cyan: #29b6f0;
    --text-light: #ffffff;
    --text-muted: #c9ccd2;
    --text-dark: #22252b;
  }
  * { box-sizing: border-box; margin: 0; padding: 0; }
  html, body { width: 1200px; height: 900px; overflow: hidden; }
  body {
    background: var(--bg);
    position: relative;
    font-family: "Poppins", sans-serif;
  }
  .card {
    position: absolute;
    left: 270px;
    width: 660px;
    height: 377px;
    overflow: hidden;
    box-shadow: 0 10px 30px rgba(0,0,0,.25);
  }
  .card--front { top: 48px; background: var(--card-black); }
  .card--back { top: 475px; background: var(--card-black); }

  /* Wordmark */
  .wordmark {
    position: absolute;
    display: flex;
    align-items: center;
    gap: 14px;
    font-family: "Marcellus", serif;
    white-space: nowrap;
  }
  .wordmark__dot {
    width: 34px; height: 34px;
    border-radius: 50%;
    background: var(--brand-blue);
    flex: none;
  }
  .wordmark__text { line-height: 1.05; }
  .wordmark__name { display: block; font-size: 42px; letter-spacing: 1px; }
  .wordmark__tag { display: block; font-size: 17px; letter-spacing: 2px; color: var(--brand-blue); }
  .card--front .wordmark {
    left: 50%; top: 140px;
    transform: translateX(-50%);
    color: var(--text-light);
  }
  .card--back .wordmark { left: 26px; top: 60px; color: var(--text-dark); }
  .card--back .wordmark__name { font-size: 32px; }
  .card--back .wordmark__tag { font-size: 13px; }
  .card--back .wordmark__dot { width: 26px; height: 26px; }

  /* Partner mark */
  .partner {
    position: absolute;
    right: 40px; bottom: 96px;
    display: flex; align-items: center; gap: 12px;
    white-space: nowrap;
  }
  .partner__lead {
    font-size: 13px;
    color: var(--text-muted);
    letter-spacing: .5px;
  }
  .partner__name {
    font-family: "Marcellus", serif;
    font-size: 26px;
    color: var(--text-light);
  }
  .partner__badge {
    width: 54px; height: 54px;
    border-radius: 50%;
    border: 3px solid var(--brand-blue);
    flex: none;
  }

  /* Back layout */
  .back-bg { position: absolute; inset: 0; }
  .gallery { position: absolute; inset: 0; }
  .gallery__tile { position: absolute; }
  .gallery__tile--product { left: 170px; top: 190px; }
  .gallery__tile--staff { left: 40px; top: 255px; }
  .gallery__tile--kitchen { left: 160px; top: 275px; }

  .contact {
    position: absolute;
    left: 350px; top: 68px;
    color: var(--text-light);
  }
  .contact__name {
    font-family: "Libre Baskerville", serif;
    font-weight: 700;
    font-size: 27px;
    color: var(--brand-blue);
    line-height: 1.1;
  }
  .contact__role { font-size: 14px; margin-top: 2px; }
  .contact__address {
    font-size: 13px;
    line-height: 1.35;
    margin-top: 46px;
    margin-left: 40px;
  }
  .contact__list {
    list-style: none;
    margin-top: 16px;
    margin-left: 40px;
    font-size: 13px;
  }
  .contact__item {
    display: flex; align-items: center; gap: 10px;
    margin-bottom: 8px;
    white-space: nowrap;
  }
  .contact__icon {
    width: 20px; height: 20px;
    border-radius: 50%;
    background: var(--accent-cyan);
    display: flex; align-items: center; justify-content: center;
    flex: none;
  }
</style>
</head>
<body>

<section class="card card--front" aria-label="Card front">
  <div class="wordmark">
    <span class="wordmark__dot"></span>
    <span class="wordmark__text">
      <span class="wordmark__name">Vera-Shine</span>
      <span class="wordmark__tag">Janitorial Services</span>
    </span>
  </div>
  <div class="partner">
    <span class="partner__lead">Powered by</span>
    <span class="partner__name">Pellmar</span>
    <span class="partner__badge" aria-label="Apex 720 system badge"></span>
  </div>
</section>

<section class="card card--back" aria-label="Card back">
  <svg class="back-bg" width="660" height="377" viewBox="0 0 660 377" aria-hidden="true">
    <rect x="0" y="0" width="660" height="377" fill="var(--card-black)"/>
    <polygon points="0,0 300,0 300,377 0,377" fill="var(--card-white)"/>
    <polygon points="300,0 312,0 312,377 300,377" fill="var(--brand-blue)"/>
    <polygon points="312,100 312,150 336,125" fill="var(--brand-blue)"/>
    <polygon points="300,108 286,125 300,142" fill="var(--brand-blue)"/>
  </svg>

  <div class="wordmark">
    <span class="wordmark__dot"></span>
    <span class="wordmark__text">
      <span class="wordmark__name">Vera-Shine</span>
      <span class="wordmark__tag">Janitorial Services</span>
    </span>
  </div>

  <div class="gallery">
    <svg class="gallery__tile gallery__tile--product" width="104" height="72" viewBox="0 0 104 72" role="img" aria-label="Photo of the Pellmar Apex 720 sprayer system">
      <defs><linearGradient id="gProduct" x1="0" y1="0" x2="1" y2="1"><stop offset="0" stop-color="#1e4fa8"/><stop offset="1" stop-color="#8fc4f0"/></linearGradient></defs>
      <polygon points="16,2 88,2 102,20 52,70 2,20" fill="url(#gProduct)" stroke="var(--brand-blue)" stroke-width="2"/>
    </svg>
    <svg class="gallery__tile gallery__tile--staff" width="104" height="72" viewBox="0 0 104 72" role="img" aria-label="Photo of a cleaner with a yellow mop bucket">
      <defs><linearGradient id="gStaff" x1="0" y1="0" x2="1" y2="1"><stop offset="0" stop-color="#7a7f86"/><stop offset="1" stop-color="#d8c24a"/></linearGradient></defs>
      <polygon points="16,2 88,2 102,20 52,70 2,20" fill="url(#gStaff)" stroke="var(--brand-blue)" stroke-width="2"/>
    </svg>
    <svg class="gallery__tile gallery__tile--kitchen" width="104" height="72" viewBox="0 0 104 72" role="img" aria-label="Photo of a kitchen being steam cleaned">
      <defs><linearGradient id="gKitchen" x1="0" y1="0" x2="1" y2="1"><stop offset="0" stop-color="#4d5560"/><stop offset="1" stop-color="#c9d3de"/></linearGradient></defs>
      <polygon points="16,2 88,2 102,20 52,70 2,20" fill="url(#gKitchen)" stroke="var(--brand-blue)" stroke-width="2"/>
    </svg>
  </div>

  <div class="contact">
    <h1 class="contact__name">Gordon Pike</h1>
    <p class="contact__role">Managing Partner</p>
    <p class="contact__address">Cedar Court 31st<br>St Elmsford, TX 79410</p>
    <ul class="contact__list">
      <li class="contact__item">
        <span class="contact__icon"><svg width="12" height="12" viewBox="0 0 24 24" aria-hidden="true"><path d="M6.6 10.8a15 15 0 0 0 6.6 6.6l2.2-2.2a1 1 0 0 1 1-.25 11.4 11.4 0 0 0 3.6.57 1 1 0 0 1 1 1V20a1 1 0 0 1-1 1A17 17 0 0 1 3 4a1 1 0 0 1 1-1h3.5a1 1 0 0 1 1 1c0 1.25.2 2.450.57 3.57a1 1 0 0 1-.25 1z" fill="#fff"/></svg></span>
        0330 5518 402
      </li>
      <li class="contact__item">
        <span class="contact__icon"><svg width="12" height="12" viewBox="0 0 24 24" aria-hidden="true"><rect x="3" y="6" width="18" height="12" rx="1" fill="none" stroke="#fff" stroke-width="2"/><path d="M3 7l9 6 9-6" fill="none" stroke="#fff" stroke-width="2"/></svg></span>
        info@verashinejanitorial.co.uk
      </li>
      <li class="contact__item">
        <span class="contact__icon"><svg width="12" height="12" viewBox="0 0 24 24" aria-hidden="true"><circle cx="12" cy="12" r="9" fill="none" stroke="#fff" stroke-width="2"/><path d="M3 12h18M12 3c3 3 3 15 0 18M12 3c-3 3-3 15 0 18" fill="none" stroke="#fff" stroke-width="1.6"/></svg></span>
        www.verashinejanitorial.co.uk
      </li>
    </ul>
  </div>
</section>

</body>
</html>
```